Pflegedienst sucht Flyerdesign
Zielgruppe
Wir sind ein ambulanter Pflegedienst und betreuen ca. 200 Patienten in ländlicher Region. Unsere Zielgruppe sind Pflegebedürftige aus altersbedingten Gründen oder nach Krankenhausaufenthalten. Wir setzen auf Qualität, Zuverlässigkeit, Exklusivität.
Aufgabenstellung
DIN lang Flyer. Wir werben ganz bewußt nicht mit Bildern von Senioren oder alten Menschen, weil das fast alle Pflegedienste tun. Daher setzen wir eher auf Motive aus unserer Urlaubsregion: Strand, Meer...
Unseren Firmen-Tarvo hätten wir gern als Fotoausschnitt ohne Hintergund mit dabei.
Und einen Kartenausschnitt mit unserem Einzugsgebiet fänden wir toll. Dies umfasst ca. 15 km um Laboe und Heikendorf folgende Orte: Stein, Wendtorf, Probsteierhagen, Schönkirchen und Mönkeberg.

```html
<!DOCTYPE html>
<html lang="de">
<head>
<meta charset="utf-8">
<title>Pflegedienst Küstenhof – Flyer</title>
<link href="https://fonts.googleapis.com/css2?family=Comfortaa:wght@300;400;700&family=Kalam:wght@400;700&family=Oswald:wght@300&display=swap" rel="stylesheet">
<style>
  :root {
    --magenta: #a8195e;
    --heading-grey: #97a8ad;
    --text: #2f3133;
    --map-land: #dce6e6;
    --map-water: #b7cccd;
    --paper: #ffffff;
  }
  * { margin: 0; padding: 0; box-sizing: border-box; }
  html, body { width: 1200px; height: 282px; overflow: hidden; background: var(--paper); }
  .flyer { position: relative; width: 1200px; height: 282px; font-family: "Comfortaa", sans-serif; color: var(--text); }
  .panel { position: absolute; top: 0; width: 400px; height: 282px; overflow: hidden; }
  .panel--team { left: 0; }
  .panel--contact { left: 400px; }
  .panel--cover { left: 800px; }

  .panel-heading { font-weight: 300; color: var(--heading-grey); font-size: 16.5px; line-height: 21.5px; letter-spacing: 0.3px; }
  .script { font-family: "Kalam", cursive; color: var(--magenta); }

  /* team panel */
  .team-heading { position: absolute; left: 20px; top: 17px; width: 200px; }
  .team-list { position: absolute; left: 26px; top: 98px; list-style: none; font-size: 7px; line-height: 9.1px; }
  .team-list li::before { content: "»"; margin-right: 5px; font-size: 6px; }
  .contacts-label { position: absolute; left: 19px; top: 197px; font-size: 8px; }
  .contacts { position: absolute; left: 18px; top: 215px; font-size: 7px; line-height: 9.1px; border-collapse: collapse; }
  .contacts td { vertical-align: top; padding: 0; }
  .contacts .name { font-family: "Kalam", cursive; color: var(--text); font-size: 6.5px; padding-right: 2px; white-space: nowrap; }
  .contacts .role { color: #55595c; }
  .team-photo { position: absolute; left: 0; top: 0; }

  /* contact panel */
  .contact-heading { position: absolute; left: 17px; top: 17px; }
  .company { position: absolute; left: 17px; top: 54px; font-size: 6.8px; font-weight: 700; }
  .address-columns { position: absolute; left: 17px; top: 72px; display: flex; font-size: 6.8px; line-height: 9px; }
  .address-columns > div { padding-right: 8px; }
  .address-columns > div + div { padding-left: 3px; border-left: 1px solid #c9d1d3; }
  .address-columns strong { font-weight: 700; }
  .address-columns .link { color: var(--magenta); }
  .service-area { position: absolute; left: 16px; top: 129px; width: 218px; height: 131px; border-radius: 9px;
    background: linear-gradient(100deg, var(--map-water) 0 18%, var(--map-land) 30% 100%); }
  .hotline { position: absolute; left: 248px; top: 156px; font-size: 11px; line-height: 15px; letter-spacing: 0.3px; }
  .brand-small { position: absolute; left: 250px; top: 238px; display: flex; align-items: center; gap: 4px; }
  .brand-small .brand-name { font-family: "Oswald", sans-serif; font-weight: 300; font-size: 6.5px; line-height: 8px; color: #7d8c91; text-align: right; letter-spacing: 0.2px; }
  .brand-small .brand-dot { width: 16px; height: 16px; border-radius: 50%; background: var(--magenta); }

  /* cover panel */
  .beach { position: absolute; left: 0; top: 0; width: 400px; height: 282px;
    background: linear-gradient(180deg, #5f97c8 0%, #8fb8de 30%, #3f7fb0 36%, #8db6cf 45%, #ece9e4 48%, #f4f3f0 70%, #dedcd8 100%); }
  .cover-curve { position: absolute; left: 0; top: 0; }
  .brand-large { position: absolute; right: 34px; top: 27px; display: flex; align-items: center; gap: 6px; }
  .brand-large .brand-name { font-family: "Oswald", sans-serif; font-weight: 300; font-size: 14.5px; line-height: 17px; color: #7d8c91; text-align: right; letter-spacing: 0.2px; }
  .brand-large .brand-dot { width: 33px; height: 33px; border-radius: 50%; background: var(--magenta); }
  .cover-title { position: absolute; left: 37px; top: 150px; font-family: "Comfortaa", sans-serif; font-weight: 400; font-size: 19.5px; line-height: 24.5px; color: #8a9599; }
  .cover-tagline { position: absolute; left: 37px; top: 205px; font-size: 12.5px; line-height: 20px; font-weight: 700; }
</style>
</head>
<body>
<main class="flyer">

  <section class="panel panel--team">
    <svg class="team-photo" width="400" height="282" viewBox="0 0 400 282" aria-hidden="false">
      <defs>
        <linearGradient id="sunset" x1="0" y1="0" x2="0" y2="1">
          <stop offset="0" stop-color="#bfc9ce"/>
          <stop offset="0.3" stop-color="#e3d5bf"/>
          <stop offset="0.44" stop-color="#f0dcb4"/>
          <stop offset="0.52" stop-color="#6d6656"/>
          <stop offset="0.62" stop-color="#cfc0a2"/>
          <stop offset="0.8" stop-color="#8c7760"/>
          <stop offset="1" stop-color="#3d2f24"/>
        </linearGradient>
      </defs>
      <path d="M246 0 C 268 80, 262 200, 212 282 L 220 282 C 270 200, 275 80, 256 0 Z" fill="var(--magenta)"/>
      <path role="img" aria-label="Foto: Abendstimmung am Wasser mit Uferlinie und Spiegelung" d="M256 0 C 275 80, 270 200, 220 282 L 400 282 L 400 0 Z" fill="url(#sunset)"/>
    </svg>

    <h2 class="panel-heading team-heading">Unser motiviertes und freundliches Team besteht aus:</h2>
    <ul class="team-list">
      <li>Examinierten Pflegefach- und Führungskräften</li>
      <li>Palliativfachkräften</li>
      <li>Wundmanagern</li>
      <li>Hygienefachkräften</li>
      <li>Pflegeberatern</li>
      <li>Haus- &amp; Familienpfleger/innen</li>
      <li>Betreuungskräften &amp; Beschäftigungsassistenten</li>
      <li>Hauswirtschaftler/innen</li>
      <li>Kaufmännischen Verwaltungskräften</li>
    </ul>

    <p class="script contacts-label">Ihre Ansprechpartner:</p>
    <table class="contacts">
      <tr><td class="name">Brunhilde Korte:</td><td class="role">Geschäftsführung</td></tr>
      <tr><td class="name">Greta Lindholm:</td><td class="role">Pflegedienstleitung,<br>Einsatzleitung Wiekdorf</td></tr>
      <tr><td class="name">Imke Petersen:</td><td class="role">Stellv. Pflegedienstleitung,<br>Einsatzleitung Seedorf</td></tr>
    </table>
  </section>

  <section class="panel panel--contact">
    <h2 class="panel-heading contact-heading">Kontakt zu uns:</h2>
    <p class="company">Pflegedienst Küstenhof GmbH</p>
    <div class="address-columns">
      <div>
        <strong>Hauptsitz:</strong><br>
        Dünenweg 7 | 24999 Seedorf<br>
        Telefon: 04300 – 12 30<br>
        Fax: 04300 – 12 31
      </div>
      <div>
        <strong>Außenstelle im Gesundheitshaus:</strong><br>
        Hafenstraße 4 | 24998 Wiekdorf<br>
        Telefon: 0400 – 98 76 50<br>
        Fax: 0400 – 98 76 51
      </div>
      <div>
        E-Mail:<br>
        <span class="link">info@pflege-kuestenhof.de</span><br>
        Internet:<br>
        <span class="link">www.pflege-kuestenhof.de</span>
      </div>
    </div>

    <div class="service-area" role="img" aria-label="Karte des Einzugsgebiets rund um die Förde mit den umliegenden Orten"></div>

    <p class="script hotline">24h-Rufbereitschaft:<br>0170 – 00 00 123</p>

    <div class="brand-small">
      <span class="brand-name">PFLEGEDIENST KÜSTENHOF<br>SEEDORF &amp; WIEKDORF</span>
      <span class="brand-dot"></span>
    </div>
  </section>

  <section class="panel panel--cover">
    <div class="beach" role="img" aria-label="Foto: Sandstrand mit Meer und blauem Himmel"></div>
    <svg class="cover-curve" width="400" height="282" viewBox="0 0 400 282" aria-hidden="true">
      <path d="M64 0 C 110 70, 220 125, 400 100 L 400 0 Z" fill="#e4e6e8"/>
      <path d="M60 0 C 105 62, 215 112, 400 92 L 400 0 Z" fill="var(--paper)"/>
    </svg>
    <div class="brand-large">
      <span class="brand-name">PFLEGEDIENST KÜSTENHOF<br>SEEDORF &amp; WIEKDORF</span>
      <span class="brand-dot"></span>
    </div>
    <h1 class="cover-title">Ihr Premiumdienst<br>in der Region</h1>
    <p class="script cover-tagline">Von Mensch zu Mensch<br>seit über 20 Jahren</p>
  </section>

</main>
</body>
</html>
```